Business card design

I have a PDF of just what I want, but I need it to be digitized for Harlow Depot so I can edit and modify for new employees and reorder going forward

Business

```html
<!DOCTYPE html>
<html lang="en">
<head>
<meta charset="utf-8">
<title>Harlow Depot – Business Cards</title>
<link rel="stylesheet" href="https://fonts.googleapis.com/css2?family=Arimo:wght@400;700&display=swap">
<style>
  :root {
    --backdrop: #5a0a02;
    --card-blue: #0879d0;
    --band-black: #0e0b09;
    --rule-white: #ffffff;
    --ink-dark: #0d0b0a;
    --ink-light: #ffffff;
    --skyline-dark: #14100e;
  }
  * { margin: 0; padding: 0; box-sizing: border-box; }
  html, body { width: 1200px; height: 1000px; overflow: hidden; }
  body {
    background: var(--backdrop);
    font-family: "Arimo", Arial, sans-serif;
    position: relative;
  }
  .card {
    position: absolute;
    top: 180px;
    width: 389px;
    height: 638px;
    background: var(--card-blue);
    box-shadow: -8px 8px 10px rgba(0,0,0,0.45);
    text-align: center;
  }
  .card--left { left: 148px; color: var(--ink-dark); }
  .card--right { left: 661px; color: var(--ink-light); }

  .brand-band {
    position: absolute;
    left: 0; top: 44px;
    width: 100%;
    height: 78px;
    background: var(--band-black);
    border-top: 2px solid var(--rule-white);
    border-bottom: 2px solid var(--rule-white);
    color: var(--ink-light);
  }
  .brand-name {
    display: block;
    margin-top: 4px;
    font-size: 40px;
    font-weight: 700;
    line-height: 42px;
    letter-spacing: 1px;
  }
  .brand-tagline {
    display: block;
    font-size: 20px;
    font-weight: 700;
    line-height: 24px;
    letter-spacing: 0.5px;
  }

  .contact {
    position: absolute;
    left: 0; top: 168px;
    width: 100%;
    font-size: 20px;
    line-height: 28px;
  }
  .contact-name { font-size: 27px; line-height: 34px; margin-bottom: -2px; }
  .contact-office { margin-top: 26px; }

  .skyline {
    position: absolute;
    left: 28px; top: 520px;
    width: 330px;
    height: 96px;
    background: linear-gradient(to bottom, rgba(20,16,14,0) 0%, rgba(20,16,14,0.55) 35%, var(--skyline-dark) 60%);
  }
</style>
</head>
<body>

  <section class="card card--left">
    <header class="brand-band">
      <span class="brand-name">HARLOW DEPOT</span>
      <span class="brand-tagline">PROPERTY MANAGERS</span>
    </header>
    <div class="contact">
      <p class="contact-name">Maren Holt</p>
      <p class="contact-role">Director/ Manager</p>
      <p class="contact-mobile">022 555 0184</p>
      <div class="contact-office">
        <p>Unit 4, 28 Quay Lane,</p>
        <p>Harbour Point, Auckland City</p>
        <p>Ph: (09) 555 0143</p>
        <p>Fax: (09) 555 0144</p>
        <p>Email: info@harlowdepot.co.nz</p>
        <p>www.harlowdepot.co.nz</p>
      </div>
    </div>
    <div class="skyline" role="img" aria-label="City skyline silhouette with a tower and a sailboat on the harbour"></div>
  </section>

  <section class="card card--right">
    <header class="brand-band">
      <span class="brand-name">HARLOW DEPOT</span>
      <span class="brand-tagline">PROPERTY MANAGERS</span>
    </header>
    <div class="contact">
      <p class="contact-name">Tobias Holt</p>
      <p class="contact-role">Director/ Manager</p>
      <p class="contact-mobile">021 555 072</p>
      <div class="contact-office">
        <p>Unit 4, 28 Quay Lane,</p>
        <p>Harbour Point, Auckland City</p>
        <p>Ph: (09) 555 0143</p>
        <p>Fax: (09) 555 0144</p>
        <p>Email: info@harlowdepot.co.nz</p>
        <p>www.harlowdepot.co.nz</p>
      </div>
    </div>
    <div class="skyline" role="img" aria-label="City skyline silhouette with a tower and a sailboat on the harbour"></div>
  </section>

</body>
</html>
```